IRON MESA TRAINING- Shooting Range!!!And virtual shooting range!!!

We are looking to do a clean cut web page for shooting range. We have indoor shooting simulator, retail store that sales accessories and pistols, rifles and shot guns. We are membership based for indoor shooting range Only and virtual shooting is open to public as well as retail store. We also specialize in shooting training classes and CWP classes.
Updates

Thank you for your patience. We are working with a busy travel schedule. We will be making final decisions tomorrow and moving forward with getting this launched. Regards, Harold

Target Market(s)

Public and private entertainment

Industry/Entity Type

Training

Number of Pages Required

5+ page

Font styles to use
Sans Serif

Requirements
Must have
• Clean and easy approach we really like the website our friend has www.vellorcrest.com please take a look at a lay out. We would like to also add onli member schedule that is available for shooting sections and that they can access and book them selvs.
Nice to have
• White, black, gray or red colors

```html
<!DOCTYPE html>
<html lang="en">
<head>
<meta charset="utf-8">
<title>Iron Mesa Training</title>
<link href="https://fonts.googleapis.com/css2?family=Titillium+Web:wght@300;400;600;700&display=swap" rel="stylesheet">
<style>
:root{
  --red:#e3212b;
  --red-dark:#c41820;
  --ink:#1c1c1c;
  --nav:#1e1e1e;
  --nav-alt:#2c2c2c;
  --grey-text:#555;
  --card:#f3f3f3;
  --light:#c9c9c9;
  --white:#fff;
  --footer:#2b2b2b;
}
*{margin:0;padding:0;box-sizing:border-box}
html,body{width:1200px;height:3303px;overflow:hidden}
body{position:relative;font-family:"Titillium Web",Arial,sans-serif;color:var(--ink);background:var(--white)}
.abs{position:absolute}

/* top strip */
.top-strip{left:0;top:0;width:1200px;height:27px;background:var(--white)}
.top-tab{top:0;height:22px;background:var(--red);color:var(--white);font-size:10px;font-weight:700;line-height:22px;text-align:center;letter-spacing:.5px}

/* header */
.header{left:0;top:27px;width:1200px;height:171px;background:var(--white)}
.round{width:38px;height:38px;border-radius:50%;background:#ececec;top:83px}
.round.red{background:var(--red)}
.search-box{top:143px;height:28px;background:var(--ink);color:#ddd;font-size:12px;line-height:28px;padding-left:10px}
.brand{left:460px;top:52px;width:280px;text-align:center}
.brand-mark{width:56px;height:56px;border-radius:50%;background:var(--red);margin:0 auto 6px}
.brand-name{font-size:30px;font-weight:700;color:var(--red);letter-spacing:1px;line-height:34px}

/* nav */
.nav{left:0;top:198px;width:1200px;height:69px;background:var(--nav)}
.nav-item{top:198px;height:69px;line-height:69px;color:#aaa;font-size:13px;font-weight:600;text-align:center;letter-spacing:.5px}
.nav-item.active{background:var(--red);color:var(--white)}
.nav-item.schedule{background:var(--nav-alt);color:var(--white)}

/* hero */
.hero{left:0;top:267px;width:1200px;height:512px;background:radial-gradient(ellipse at 50% 70%,#8a6a4a 0%,#4e3a28 45%,#241a12 100%)}
.hero-title{left:0;top:368px;width:1200px;text-align:center;color:var(--white);font-size:50px;line-height:58px;font-weight:300}
.hero-title b{font-weight:700}
.btn{display:block;text-align:center;font-weight:700;font-size:12px;color:var(--white);letter-spacing:.5px}
.btn-red{background:var(--red)}
.btn-dark{background:#2e2e2e}
.hero-arrow{top:493px;width:54px;height:54px;border-radius:50%;border:2px solid rgba(255,255,255,.8)}
.dot{top:656px;width:10px;height:10px;border-radius:50%;background:rgba(255,255,255,.6)}

/* section titles */
.sec-title{left:0;width:1200px;text-align:center;font-size:38px;font-weight:300;letter-spacing:5px}
.sec-title span{color:var(--red);font-weight:600}
.sec-sub{left:0;width:1200px;text-align:center;font-size:12px;letter-spacing:2px;color:#999}
.sec-sub i{display:inline-block;width:60px;height:1px;background:#ccc;vertical-align:middle;margin:0 14px}

/* feature cards */
.card{top:930px;width:247px;height:372px;background:var(--card);text-align:center}
.card svg{margin-top:42px}
.card-title{margin:22px 24px 0;padding-top:14px;border-top:1px solid #ddd;font-size:18px;font-weight:700}
.card-title span{font-weight:400}
.card-text{margin:14px 24px 0;font-size:11px;line-height:16px;color:var(--grey-text);text-align:left}
.card .btn{width:132px;height:47px;line-height:47px;margin:22px auto 0}

/* specialize */
.special{left:0;top:1357px;width:1200px;height:523px;background:linear-gradient(90deg,#151515 0%,#2a2a2a 45%,#3a3530 70%,#1a1a1a 100%)}
.special-title{color:var(--white)}
.special-sub{color:#ddd}
.special-sub i{background:#777}
.special-label{top:1690px;width:300px;text-align:center;color:var(--white);font-size:16px;font-weight:600}
.special-btn{top:1783px;width:160px;height:44px;line-height:44px;background:var(--light);color:#333;font-size:12px;font-weight:700;text-align:center}

/* services */
.tile{width:298px;height:218px}
.caption{width:298px;height:57px;background:var(--white);border-bottom:1px solid #e6e6e6;padding:12px 0 0 14px}
.caption h4{font-size:13px;font-weight:700;line-height:16px}
.caption p{font-size:11px;color:#888;line-height:16px}
.caption svg{position:absolute;right:14px;top:14px}

/* footer */
.footer{left:0;top:2747px;width:1200px;height:468px;background:linear-gradient(180deg,#2f2f2f,#262626)}
.footer-name{left:0;top:2888px;width:1200px;text-align:center;color:var(--white);font-size:40px;font-weight:600;letter-spacing:1px}
.footer-rule{left:420px;top:2960px;width:360px;height:1px;background:#666}
.footer-addr{left:0;top:2978px;width:1200px;text-align:center;color:#ccc;font-size:13px}
.contact-box{top:3035px;width:248px;height:116px;border:1px solid #555;text-align:center;color:var(--white);font-size:17px;padding-top:24px}
.contact-box div{margin-top:10px}
.bottom-bar{left:0;top:3215px;width:1200px;height:88px;background:var(--red)}
.copyright{left:170px;top:3250px;color:var(--white);font-size:11px;font-weight:600;letter-spacing:.5px}
.social-sq{top:3215px;width:50px;height:88px;border-left:1px solid rgba(255,255,255,.25)}
.social-sq span{display:block;width:12px;height:12px;border-radius:50%;background:rgba(255,255,255,.85);margin:38px auto 0}
</style>
</head>
<body>

<!-- top strip -->
<div class="abs top-strip"></div>
<div class="abs top-tab" style="left:170px;width:78px">LOGIN</div>
<div class="abs top-tab" style="left:250px;width:80px">REGISTER</div>
<div class="abs top-tab" style="left:950px;width:56px">SHOP</div>

<!-- header -->
<header class="abs header"></header>
<div class="abs round" style="left:174px"></div>
<div class="abs round" style="left:231px"></div>
<div class="abs round" style="left:286px"></div>
<div class="abs round red" style="left:339px"></div>
<div class="abs search-box" style="left:267px;width:173px">search</div>
<div class="abs brand"><div class="brand-mark"></div><div class="brand-name">IRON MESA</div></div>
<div class="abs round red" style="left:751px"></div>
<div class="abs round" style="left:815px"></div>
<div class="abs round" style="left:875px"></div>
<div class="abs round" style="left:933px"></div>
<div class="abs search-box" style="left:757px;width:173px">Social</div>

<!-- nav -->
<nav class="abs nav"></nav>
<div class="abs nav-item active" style="left:170px;width:138px">HOME</div>
<div class="abs nav-item" style="left:322px;width:100px">ABOUT</div>
<div class="abs nav-item" style="left:454px;width:100px">CLASSES</div>
<div class="abs nav-item" style="left:583px;width:100px">SHOP</div>
<div class="abs nav-item" style="left:710px;width:100px">CONTACT</div>
<div class="abs nav-item schedule" style="left:834px;width:196px">ONLINE MEMBER SCHEDULE</div>

<!-- hero -->
<section class="abs hero" role="img" aria-label="Hearing protection earmuffs and a pistol on a shooting range bench"></section>
<h1 class="abs hero-title">THE MOST <b>INNOVATIVE TRAINING</b><br>&amp; HIGHEST <b>PERFORMANCE GEAR !</b></h1>
<a class="abs btn btn-red" style="left:504px;top:512px;width:187px;height:60px;line-height:60px">JOIN TODAY !</a>
<div class="abs hero-arrow" style="left:50px"><svg width="50" height="50"><path d="M28 17 L20 25 L28 33" stroke="#fff" stroke-width="2" fill="none"/></svg></div>
<div class="abs hero-arrow" style="left:1088px"><svg width="50" height="50"><path d="M22 17 L30 25 L22 33" stroke="#fff" stroke-width="2" fill="none"/></svg></div>
<div class="abs dot" style="left:582px;background:#fff"></div>
<div class="abs dot" style="left:597px"></div>
<div class="abs dot" style="left:612px"></div>

<!-- welcome -->
<h2 class="abs sec-title" style="top:818px">WELCOME TO THE <span>IRON MESA !</span></h2>
<div class="abs sec-sub" style="top:887px"><i></i>TRAINING LLC<i></i></div>

<div class="abs card" style="left:193px">
  <svg width="100" height="86" viewBox="0 0 100 86"><path d="M8 40 L50 6 L92 40" stroke="#555" stroke-width="7" fill="none"/><path d="M20 36 V82 H80 V36" stroke="#555" stroke-width="6" fill="none"/><circle cx="50" cy="56" r="16" fill="none" stroke="#e3212b" stroke-width="5"/><circle cx="50" cy="56" r="6" fill="#e3212b"/></svg>
  <div class="card-title">INDOOR <span>SHOOTING</span></div>
  <p class="card-text">Members book lanes, bring their gear and train in a safe, climate controlled indoor range with staff on hand every day.</p>
  <a class="btn btn-red">READ MORE</a>
</div>
<div class="abs card" style="left:476px">
  <svg width="100" height="86" viewBox="0 0 100 86"><circle cx="50" cy="43" r="36" fill="none" stroke="#555" stroke-width="7"/><circle cx="50" cy="43" r="18" fill="none" stroke="#e3212b" stroke-width="6"/><circle cx="50" cy="43" r="6" fill="#555"/><path d="M50 0 V20 M50 66 V86 M7 43 H27 M73 43 H93" stroke="#555" stroke-width="5"/></svg>
  <div class="card-title">VIRTUAL <span>SHOOTING</span></div>
  <p class="card-text">Our simulator is open to the public, with lifelike drills and scenarios that sharpen focus, speed and decision making.</p>
  <a class="btn btn-dark">READ MORE</a>
</div>
<div class="abs card" style="left:757px">
  <svg width="100" height="86" viewBox="0 0 100 86"><path d="M6 14 H22 L34 60 H80 L90 26 H30" stroke="#555" stroke-width="6" fill="none"/><circle cx="40" cy="74" r="7" fill="#555"/><circle cx="74" cy="74" r="7" fill="#555"/><rect x="40" y="10" width="14" height="12" fill="#e3212b"/><rect x="58" y="4" width="16" height="18" fill="#e3212b"/></svg>
  <div class="card-title">RETAIL <span>STORE</span></div>
  <p class="card-text">Shop pistols, rifles, shotguns and accessories, with friendly advice from staff who know every item on the shelf.</p>
  <a class="btn btn-dark">READ MORE</a>
</div>

<!-- specialize -->
<section class="abs special" role="img" aria-label="Shooter aiming at an indoor range seen from the side in dim light"></section>
<h2 class="abs sec-title special-title" style="top:1400px">WE ALSO <span>SPECIALIZE</span> IN</h2>
<div class="abs sec-sub special-sub" style="top:1482px"><i></i>SHOOT TRAINING CLASSES &amp; CWP CLASSES<i></i></div>
<svg class="abs" style="left:362px;top:1582px" width="30" height="86" viewBox="0 0 30 86"><path d="M15 0 C24 10 26 22 26 30 V80 H4 V30 C4 22 6 10 15 0 Z" fill="#e3212b"/><rect x="4" y="42" width="22" height="4" fill="#1c1c1c"/></svg>
<div class="abs" style="left:596px;top:1632px;width:3px;height:22px;background:#fff"></div>
<svg class="abs" style="left:808px;top:1580px" width="90" height="90" viewBox="0 0 90 90"><circle cx="45" cy="45" r="34" fill="none" stroke="#e3212b" stroke-width="7"/><circle cx="45" cy="45" r="16" fill="#e3212b"/><path d="M45 0 V24 M45 66 V90 M0 45 H24 M66 45 H90" stroke="#e3212b" stroke-width="5"/></svg>
<div class="abs special-label" style="left:227px">CWP CLASSES</div>
<div class="abs special-label" style="left:703px">SHOOTING TRAINING CLASSES</div>
<div class="abs special-btn" style="left:344px">RESERVE</div>
<div class="abs special-btn" style="left:523px">SCHEDULE</div>
<div class="abs special-btn" style="left:696px">FOLLOW</div>

<!-- services -->
<h2 class="abs sec-title" style="top:1918px">OUR AWESOME <span>SERVICES !</span></h2>
<div class="abs sec-sub" style="top:1988px"><i></i>SERVICES<i></i></div>

<div class="abs tile" style="left:0;top:2042px;background:linear-gradient(135deg,#8a8f96,#3d434a)" role="img" aria-label="Instructor coaching a student at a shooting lane"></div>
<div class="abs tile" style="left:301px;top:2042px;background:linear-gradient(135deg,#3a5a8a,#16243a)" role="img" aria-label="Row of shooters at indoor range lanes"></div>
<div class="abs tile" style="left:602px;top:2042px;background:linear-gradient(135deg,#d9d4c8,#6b6558)" role="img" aria-label="Pistols and ammunition on a table"></div>
<div class="abs tile" style="left:903px;top:2042px;background:linear-gradient(135deg,#e8e8e8,#9a9a9a)" role="img" aria-label="Empty bright range lane with targets"></div>
<div class="abs caption" style="left:0;top:2260px"><h4>LOREM IPSUM DOLOR SIT AMET</h4><p>adipiscing elit, sed diam nonummy.</p><svg width="14" height="14"><circle cx="6" cy="6" r="4.5" stroke="#e3212b" stroke-width="2" fill="none"/><path d="M9 9 L13 13" stroke="#e3212b" stroke-width="2"/></svg></div>
<div class="abs caption" style="left:301px;top:2260px"><h4>LOREM IPSUM DOLOR SIT AMET</h4><p>adipiscing elit, sed diam nonummy.</p><svg width="14" height="14"><circle cx="6" cy="6" r="4.5" stroke="#e3212b" stroke-width="2" fill="none"/><path d="M9 9 L13 13" stroke="#e3212b" stroke-width="2"/></svg></div>
<div class="abs caption" style="left:602px;top:2260px"><h4>LOREM IPSUM DOLOR SIT AMET</h4><p>adipiscing elit, sed diam nonummy.</p><svg width="14" height="14"><circle cx="6" cy="6" r="4.5" stroke="#e3212b" stroke-width="2" fill="none"/><path d="M9 9 L13 13" stroke="#e3212b" stroke-width="2"/></svg></div>
<div class="abs caption" style="left:903px;top:2260px"><h4>LOREM IPSUM DOLOR SIT AMET</h4><p>adipiscing elit, sed diam nonummy.</p><svg width="14" height="14"><circle cx="6" cy="6" r="4.5" stroke="#e3212b" stroke-width="2" fill="none"/><path d="M9 9 L13 13" stroke="#e3212b" stroke-width="2"/></svg></div>

<div class="abs tile" style="left:0;top:2320px;background:linear-gradient(135deg,#b0672a,#3a2414)" role="img" aria-label="Shooter wearing ear protection in warm light"></div>
<div class="abs tile" style="left:301px;top:2320px;background:linear-gradient(135deg,#8a6a4c,#2e2218)" role="img" aria-label="Handgun and cartridges on a wooden surface"></div>
<div class="abs tile" style="left:602px;top:2320px;background:linear-gradient(135deg,#6a6a6a,#222)" role="img" aria-label="Two shooters aiming inside a range booth"></div>
<div class="abs tile" style="left:903px;top:2320px;background:linear-gradient(135deg,#4a4a4a,#151515)" role="img" aria-label="Rifle resting on a dark gear bag"></div>
<div class="abs caption" style="left:0;top:2538px"><h4>LOREM IPSUM DOLOR SIT AMET</h4><p>adipiscing elit, sed diam nonummy.</p><svg width="14" height="14"><circle cx="6" cy="6" r="4.5" stroke="#e3212b" stroke-width="2" fill="none"/><path d="M9 9 L13 13" stroke="#e3212b" stroke-width="2"/></svg></div>
<div class="abs caption" style="left:301px;top:2538px"><h4>LOREM IPSUM DOLOR SIT AMET</h4><p>adipiscing elit, sed diam nonummy.</p><svg width="14" height="14"><circle cx="6" cy="6" r="4.5" stroke="#e3212b" stroke-width="2" fill="none"/><path d="M9 9 L13 13" stroke="#e3212b" stroke-width="2"/></svg></div>
<div class="abs caption" style="left:602px;top:2538px"><h4>LOREM IPSUM DOLOR SIT AMET</h4><p>adipiscing elit, sed diam nonummy.</p><svg width="14" height="14"><circle cx="6" cy="6" r="4.5" stroke="#e3212b" stroke-width="2" fill="none"/><path d="M9 9 L13 13" stroke="#e3212b" stroke-width="2"/></svg></div>
<div class="abs caption" style="left:903px;top:2538px"><h4>LOREM IPSUM DOLOR SIT AMET</h4><p>adipiscing elit, sed diam nonummy.</p><svg width="14" height="14"><circle cx="6" cy="6" r="4.5" stroke="#e3212b" stroke-width="2" fill="none"/><path d="M9 9 L13 13" stroke="#e3212b" stroke-width="2"/></svg></div>

<a class="abs btn btn-red" style="left:506px;top:2642px;width:187px;height:61px;line-height:61px">SEE MORE SERVICES !</a>

<!-- footer -->
<footer class="abs footer" role="img" aria-label="Faint street map background"></footer>
<svg class="abs" style="left:580px;top:2840px" width="40" height="56" viewBox="0 0 40 56"><path d="M20 3 C10 3 4 10 4 19 C4 31 20 46 20 46 C20 46 36 31 36 19 C36 10 30 3 20 3 Z" fill="none" stroke="#fff" stroke-width="3"/><circle cx="20" cy="19" r="6" fill="none" stroke="#fff" stroke-width="3"/><ellipse cx="20" cy="51" rx="14" ry="3" fill="none" stroke="#fff" stroke-width="2"/></svg>
<div class="abs footer-name">IRON MESA</div>
<div class="abs footer-rule"></div>
<div class="abs footer-addr"><b>Unit 9</b> Range Road, Mesa Valley, open daily from nine until late evening.</div>
<div class="abs contact-box" style="left:228px"><svg width="26" height="26" viewBox="0 0 24 24"><path d="M6 2 L10 7 L8 10 C9 12 12 15 14 16 L17 14 L22 18 L19 22 C10 21 3 14 2 5 Z" fill="#fff"/></svg><div>0800-555-0142</div></div>
<div class="abs contact-box" style="left:476px"><svg width="26" height="26" viewBox="0 0 24 24"><rect x="6" y="2" width="12" height="6" fill="#fff"/><rect x="2" y="9" width="20" height="9" rx="2" fill="#fff"/><rect x="6" y="15" width="12" height="7" fill="#fff" stroke="#2b2b2b" stroke-width="1.5"/></svg><div>0800-555-0142</div></div>
<div class="abs contact-box" style="left:724px"><svg width="28" height="26" viewBox="0 0 26 24"><path d="M2 8 L24 2 L18 22 L12 14 Z" fill="none" stroke="#fff" stroke-width="2"/><path d="M12 14 L24 2" stroke="#fff" stroke-width="2"/></svg><div>desk@ironmesarange.com</div></div>

<div class="abs bottom-bar"></div>
<div class="abs copyright">IRON MESA © 2015. ALL RIGHTS RESERVED</div>
<div class="abs social-sq" style="left:830px"><span></span></div>
<div class="abs social-sq" style="left:880px"><span></span></div>
<div class="abs social-sq" style="left:930px"><span></span></div>
<div class="abs social-sq" style="left:980px;border-right:1px solid rgba(255,255,255,.25)"><span></span></div>

</body>
</html>
```